Private Optometric Practice Needs new Presentation Folders/Stationary

We recently moved our office and are looking to refresh our presentation folders and stationary. I tend to prefer simple, clean designs. We are a full scope optometric practice provide high quality eyewear, custom contact lenses, along with emergency care and treatment for dry eyes. We communicate with a lot of other doctors and want to exude professionalism. I have attached 2 versions of our logo.

Target Market(s)

Familys

Industry/Entity Type

Eyecare

Font styles to use
Sans Serif

Colors
0054AA
0677BA
7BADD7
CADEEF
E8F1F8

Requirements
Nice to have
• Bifold, areas to put information about practice, welcome letter

```html
<!DOCTYPE html>
<html lang="en">
<head>
<meta charset="utf-8">
<title>Brightwell Vision — Stationery and Folders</title>
<link rel="stylesheet" href="https://fonts.googleapis.com/css2?family=Montserrat:wght@400;500&family=Open+Sans:wght@400;600&family=Playfair+Display+SC&family=Dancing+Script:wght@500&display=swap">
<style>
  :root{
    --blue:#2e9dd6;
    --blue-deep:#2486bd;
    --blue-pale:#e8f1f8;
    --blue-mist:#cadeef;
    --grey:#6b6b6b;
    --grey-dark:#4a4a4a;
    --paper:#ffffff;
    --bg-top:#f1f1f1;
    --bg-mid:#d8d8d8;
    --bg-low:#e2e2e2;
  }
  *{box-sizing:border-box;margin:0;padding:0}
  html,body{width:1200px;height:2489px;overflow:hidden}
  body{position:relative;font-family:"Open Sans",Arial,sans-serif;color:var(--grey-dark)}
  .scene{position:absolute;left:0;width:1200px}
  .scene--stationery{top:0;height:800px;background:var(--bg-top)}
  .scene--pocket{top:800px;height:870px;background:var(--bg-mid)}
  .scene--bifold{top:1670px;height:819px;background:var(--bg-low)}
  .piece{position:absolute;background:var(--paper);box-shadow:0 2px 6px rgba(0,0,0,.15);overflow:hidden}

  /* brand name block */
  .brand{display:flex;flex-direction:column;align-items:center;font-family:"Montserrat",Arial,sans-serif;font-weight:400;color:var(--blue);text-transform:uppercase;letter-spacing:.22em;line-height:1.15;text-align:center}
  .brand__dot{border-radius:50%;background:currentColor;margin-bottom:.35em}
  .brand--white{color:#fff}

  /* letterhead */
  .letterhead{left:300px;top:100px;width:300px;height:425px}
  .letterhead .brand{position:absolute;left:28px;top:28px;font-size:8px;align-items:flex-start}
  .letterhead .brand__dot{width:14px;height:14px}
  .letter{position:absolute;left:32px;top:100px;width:240px;font-size:4.6px;line-height:1.65;color:#555}
  .letter p{margin-bottom:6px}
  .letter-foot{position:absolute;left:32px;right:28px;top:383px;border-top:.6px solid #bbb;padding-top:6px;display:flex;justify-content:space-between;font-size:4.4px;line-height:1.5;color:#555}
  .band{position:absolute;left:0;right:0;bottom:0;height:5px;background:linear-gradient(100deg,var(--blue) 0 66%,var(--grey) 66% 100%)}

  /* presentation cover */
  .cover{left:660px;top:80px;width:355px;height:455px;border-left:6px double #ddd}
  .cover .brand{position:absolute;left:0;right:0;top:180px;font-size:24px;color:var(--grey)}
  .cover .brand__dot{width:52px;height:52px;color:var(--blue)}
  .tagline{position:absolute;left:0;right:0;top:400px;text-align:center;font-family:"Playfair Display SC",Georgia,serif;font-size:13px;color:var(--grey-dark)}
  .tagline em{font-family:"Dancing Script",cursive;font-style:normal;font-size:17px;color:var(--blue)}

  /* business cards */
  .card-front{left:193px;top:570px;width:137px;height:77px;background:var(--blue)}
  .card-front .brand{position:absolute;inset:0;justify-content:center;font-size:7px}
  .card-front .brand__dot{width:14px;height:14px}
  .card-back{left:193px;top:670px;width:137px;height:77px}
  .card-back .brand{position:absolute;right:10px;top:8px;font-size:5px}
  .card-back .brand__dot{width:9px;height:9px}
  .card-info{position:absolute;left:9px;top:38px;font-size:3.6px;line-height:1.5;color:#555}
  .card-info .title{color:var(--blue)}
  .card-addr{position:absolute;right:9px;top:52px;font-size:3.4px;line-height:1.45;text-align:right;color:#555}
  .card-back .band{height:3px}

  /* envelopes */
  .env-front{left:365px;top:580px;width:340px;height:162px;background:#f9f9f9}
  .env-front .brand{position:absolute;left:22px;top:20px;font-size:8px}
  .env-front .brand__dot{width:14px;height:14px}
  .env-addr{position:absolute;left:22px;top:56px;font-size:4.4px;line-height:1.5;color:#555}
  .env-mark{position:absolute;left:190px;top:30px;width:110px;height:110px;border-radius:50%;background:var(--blue-pale)}
  .env-back{left:738px;top:580px;width:340px;height:162px}
  .env-flap{position:absolute;left:0;right:0;top:0;height:58px;background:var(--blue)}
  .env-flap .brand{position:absolute;inset:0;justify-content:center;font-size:7px}
  .env-flap .brand__dot{width:13px;height:13px}

  /* pocket folder */
  .pocket-cover{left:110px;top:150px;width:300px;height:580px;background:var(--blue)}
  .pocket-cover svg{position:absolute;inset:0}
  .pocket-cover .brand{position:absolute;left:0;right:0;top:140px;font-size:27px}
  .pocket-cover .brand__dot{width:58px;height:58px}
  .pocket-inside{left:570px;top:185px;width:562px;height:520px}
  .pocket-pattern{position:absolute;left:0;top:0;width:100%;height:360px;background:linear-gradient(90deg,#f6f6f6 0 50%,#e8ebee 50% 100%)}
  .pocket-fold{position:absolute;left:280px;top:0;width:2px;height:100%;background:#c9c9c9}
  .pocket-flap{position:absolute;top:360px;height:160px;width:280px;background:var(--blue)}
  .pocket-flap--left{left:0;background:#45ade3}
  .pocket-flap--right{left:282px}
  .tucked-card{position:absolute;left:350px;top:390px;width:122px;height:70px;background:#fff;box-shadow:0 2px 4px rgba(0,0,0,.2)}
  .tucked-card .brand{position:absolute;right:8px;top:6px;font-size:4.4px}
  .tucked-card .brand__dot{width:8px;height:8px}
  .tucked-card .card-info{left:8px;top:34px;font-size:3.2px}
  .tucked-card .card-addr{right:8px;top:46px;font-size:3px}

  /* bifold */
  .bifold{left:150px;top:180px;width:900px;height:580px;background:#fff}
  .bifold svg{position:absolute;inset:0}
  .bifold-front .brand{position:absolute;left:450px;width:450px;top:110px;font-size:27px}
  .bifold-front .brand__dot{width:58px;height:58px}
  .bifold-back{position:absolute;left:0;width:450px;top:390px;display:flex;flex-direction:column;align-items:center}
  .bifold-back .brand{font-size:19px}
  .bifold-back .brand__dot{width:42px;height:42px}
  .bifold-contact{margin-top:16px;text-align:center;font-size:11px;line-height:1.55;color:var(--grey-dark)}
  .bifold-contact b{color:var(--blue);font-weight:600}
</style>
</head>
<body>

<section class="scene scene--stationery">
  <article class="piece letterhead">
    <div class="brand"><span class="brand__dot"></span>Brightwell<br>Vision</div>
    <div class="letter">
      <p>Dear customer,</p>
      <p>Thank you for choosing our practice for your family's eye care. Our team offers complete exams, quality eyewear and custom contact lenses in a calm, welcoming setting.</p>
      <p>We also provide emergency visits and treatment for dry eyes, and we work closely with your other doctors so that every step of your care stays connected.</p>
      <p>Our new office has more exam rooms, a larger frame gallery and easy parking. Please call us with any questions before your first appointment.</p>
      <p>We look forward to seeing you and caring for your vision.</p>
      <p>Yours Sincerely,</p>
    </div>
    <div class="letter-foot">
      <div>1420 Maple Grove Ave, Suite B<br>Lakeford, OH 44012</div>
      <div>(555) 014-2290<br>hello@brightwellvision.com<br>www.brightwellvision.com</div>
    </div>
    <div class="band"></div>
  </article>

  <article class="piece cover">
    <div class="brand"><span class="brand__dot"></span>Brightwell<br>Vision</div>
    <p class="tagline">Eyesight is <em>precious</em></p>
  </article>

  <article class="piece card-front">
    <div class="brand brand--white"><span class="brand__dot"></span>Brightwell<br>Vision</div>
  </article>
  <article class="piece card-back">
    <div class="brand"><span class="brand__dot"></span>Brightwell<br>Vision</div>
    <div class="card-info">DANIEL MORROW, O.D.<br><span class="title">Optometrist</span><br>(555) 014-2290<br>hello@brightwellvision.com<br>www.brightwellvision.com</div>
    <div class="card-addr">1420 Maple Grove Ave<br>Suite B<br>Lakeford, OH 44012</div>
    <div class="band"></div>
  </article>

  <article class="piece env-front">
    <div class="env-mark"></div>
    <div class="brand"><span class="brand__dot"></span>Brightwell<br>Vision</div>
    <div class="env-addr">1420 Maple Grove Ave, Suite B<br>Lakeford, OH 44012</div>
    <div class="band"></div>
  </article>
  <article class="piece env-back">
    <div class="env-flap"><div class="brand brand--white"><span class="brand__dot"></span>Brightwell<br>Vision</div></div>
  </article>
</section>

<section class="scene scene--pocket">
  <article class="piece pocket-cover">
    <svg viewBox="0 0 300 580" width="300" height="580" aria-hidden="true">
      <path d="M0,300 C50,430 150,530 300,580 L0,580 Z" fill="#fff"/>
      <path d="M0,318 C55,440 150,535 255,580" fill="none" stroke="#6b6b6b" stroke-width="4"/>
    </svg>
    <div class="brand brand--white"><span class="brand__dot"></span>Brightwell<br>Vision</div>
  </article>

  <article class="piece pocket-inside">
    <div class="pocket-pattern" role="img" aria-label="Repeating embossed brand pattern across the inside panels"></div>
    <div class="pocket-fold"></div>
    <div class="pocket-flap pocket-flap--left"></div>
    <div class="pocket-flap pocket-flap--right"></div>
    <div class="tucked-card">
      <div class="brand"><span class="brand__dot"></span>Brightwell<br>Vision</div>
      <div class="card-info">DANIEL MORROW, O.D.<br>(555) 014-2290<br>hello@brightwellvision.com</div>
      <div class="card-addr">1420 Maple Grove Ave<br>Lakeford, OH 44012</div>
    </div>
  </article>
</section>

<section class="scene scene--bifold">
  <article class="piece bifold">
    <svg viewBox="0 0 900 580" width="900" height="580" aria-hidden="true">
      <path d="M0,0 L900,0 L900,440 C700,460 560,340 450,210 C350,70 150,0 0,25 Z" fill="#2e9dd6"/>
      <path d="M0,25 C150,0 350,70 450,210" fill="none" stroke="#2486bd" stroke-width="0"/>
      <path d="M60,16 C220,10 380,110 470,250 C570,380 720,470 880,458" fill="none" stroke="#6b6b6b" stroke-width="5"/>
      <path d="M0,25 C150,0 350,70 450,210 C560,340 700,460 900,440" fill="none" stroke="#fff" stroke-width="6"/>
      <line x1="450" y1="0" x2="450" y2="580" stroke="#000" stroke-opacity=".08" stroke-width="2"/>
    </svg>
    <div class="bifold-front"><div class="brand brand--white"><span class="brand__dot"></span>Brightwell<br>Vision</div></div>
    <div class="bifold-back">
      <div class="brand"><span class="brand__dot"></span>Brightwell<br>Vision</div>
      <p class="bifold-contact"><b>T :</b> (555) 014-2290<br>www.brightwellvision.com<br>1420 Maple Grove Ave, Suite B, Lakeford, OH 44012</p>
    </div>
  </article>
</section>

</body>
</html>
```